New Gin label required for the launch of our second gin brand.

We are a small independent pub and are due to launch our second Gin and require a label design for the bottle. This will be a pink gin.
We are based in the Old Swan area of Liverpool, UK and I'm looking for a modern, sleek, clean design.
Colours and design styles are your choice and you may incorporate a swan. We have not decided on the name of the gin, so If you could use 'The Brindle Yard Pink Gin' or 'The Brindle Yard Gin #2', that would be great.
The bottle will be 70cl and the abv will be 42%

```html
<!DOCTYPE html>
<html lang="en">
<head>
<meta charset="utf-8">
<title>The Brindle Yard Pink Gin – Label</title>
<link rel="stylesheet" href="https://fonts.googleapis.com/css2?family=Libre+Baskerville:wght@700&family=Pinyon+Script&family=Lato:wght@700;900&display=swap">
<style>
  :root {
    --bg: #eceef1;
    --ink: #111111;
    --paper: #ffffff;
    --swan-light: #f4f4f4;
    --swan-dark: #b9bcc0;
  }
  html, body {
    margin: 0;
    padding: 0;
    overflow: hidden;
  }
  body {
    width: 801px;
    height: 1200px;
    background: var(--bg);
    position: relative;
    color: var(--ink);
    font-family: "Lato", sans-serif;
  }
  .label {
    position: absolute;
    left: 0;
    top: 0;
    width: 801px;
    height: 1200px;
    text-align: center;
  }
  .edition {
    position: absolute;
    top: 524px;
    left: 0;
    right: 0;
    font-weight: 700;
    font-size: 11px;
    line-height: 15px;
    letter-spacing: 0.2px;
  }
  .title-the {
    position: absolute;
    top: 568px;
    left: 0;
    right: 0;
    font-family: "Pinyon Script", cursive;
    font-size: 34px;
    line-height: 40px;
  }
  .flourish {
    position: absolute;
    top: 586px;
    left: 280px;
    width: 241px;
    height: 12px;
  }
  .brand-name {
    position: absolute;
    top: 614px;
    left: 0;
    right: 0;
    font-family: "Libre Baskerville", serif;
    font-weight: 700;
    font-size: 32px;
    line-height: 40px;
    letter-spacing: 0.5px;
    margin: 0;
  }
  .product-name {
    position: absolute;
    top: 656px;
    left: 0;
    right: 0;
    font-family: "Libre Baskerville", serif;
    font-weight: 700;
    font-size: 27px;
    line-height: 36px;
    letter-spacing: 0.5px;
    margin: 0;
  }
  .swan-art {
    position: absolute;
    left: 296px;
    top: 700px;
    width: 204px;
    height: 136px;
    background: linear-gradient(180deg, var(--swan-light) 0%, var(--swan-dark) 100%);
    border-radius: 6px;
  }
  .claim {
    position: absolute;
    top: 853px;
    left: 290px;
    width: 222px;
    height: 22px;
    border-radius: 11px;
    background: var(--ink);
    color: var(--paper);
    font-weight: 700;
    font-size: 12.5px;
    line-height: 22px;
    letter-spacing: 0.3px;
  }
  .recipe {
    position: absolute;
    top: 879px;
    left: 0;
    right: 0;
    font-weight: 700;
    font-size: 10.5px;
    line-height: 14px;
    letter-spacing: 0.2px;
  }
  .volume {
    position: absolute;
    top: 911px;
    left: 0;
    right: 0;
    font-weight: 700;
    font-size: 10.5px;
    line-height: 14px;
  }
</style>
</head>
<body>
  <main class="label">
    <div class="edition">LIMITED EDITION<br>EST. 2018</div>

    <svg class="flourish" viewBox="0 0 241 12" aria-hidden="true">
      <path d="M0 7 Q44 4 88 6" fill="none" stroke="#111" stroke-width="1.6" stroke-linecap="round"/>
      <path d="M153 6 Q197 4 241 7" fill="none" stroke="#111" stroke-width="1.6" stroke-linecap="round"/>
    </svg>
    <div class="title-the">The</div>

    <h1 class="brand-name">BRINDLE YARD</h1>
    <h2 class="product-name">PINK GIN</h2>

    <div class="swan-art" role="img" aria-label="Engraved-style illustration of a swan gliding on rippling water"></div>

    <div class="claim">THE WORLD'S FIRST PINK GIN</div>
    <div class="recipe">THE ORIGINAL RECIPE BY PROJECT OWNER</div>
    <div class="volume">500ml / 70cl &nbsp;42%ABV</div>
  </main>
</body>
</html>
```